New website for Pilates Studio

I need a new version of my website
http://brightcoreflow.biz/
I want an updated fresh look with an easier to read schedule that looks good on mobile phones as well as laptops.
Clean, simple, fresh and BOLD

Target Market(s)

All ages, genders and races

Coding

Number of Pages Required

Colors
9bcb3c

Requirements
Must have
• Photos that mostly use the real images from our studio. Browse our facebook page, website or ask me for high quality images

```html
<!DOCTYPE html>
<html lang="en">
<head>
<meta charset="utf-8">
<title>Bright Core Flow – Pilates & Spiral Motion Studio</title>
<link rel="stylesheet" href="https://fonts.googleapis.com/css2?family=Roboto+Condensed:wght@400;700&family=Open+Sans:wght@400;600;700&family=Arimo:wght@400;700&display=swap">
<style>
:root{
  --green:#7aa026;
  --green-dark:#5f8a1c;
  --green-deep:#2f4d10;
  --gold:#c9a43a;
  --gold-btn:#d4a52b;
  --text:#555;
  --muted:#777;
  --line:#e4e4e4;
  --band:#ededed;
  --card:#ddd6bd;
  --footer:#333;
  --chip:#8c8c8c;
}
*{box-sizing:border-box;margin:0;padding:0}
html,body{width:750px;height:1200px;overflow:hidden;background:#fff}
body{position:relative;font-family:"Open Sans",sans-serif;color:var(--text)}
h1,h2{font-weight:400}

/* header */
.brand{position:absolute;left:63px;top:18px;display:flex;align-items:center;gap:8px}
.brand-dot{width:36px;height:36px;border-radius:50%;background:var(--gold)}
.brand-name{font-family:"Arimo",sans-serif;font-size:24px;font-weight:700;color:var(--green-dark)}
.contact{position:absolute;left:553px;top:15px;font-family:"Arimo",sans-serif;font-size:8px;color:#222;line-height:13px}
.contact svg{vertical-align:-1px;margin-right:4px}
.follow{position:absolute;left:536px;top:49px;display:flex;align-items:center;gap:4px;font-family:"Arimo",sans-serif;font-size:8.5px;color:#222}
.follow span{margin-right:5px}
.follow i{display:block;width:19px;height:19px;border-radius:3px;background:var(--chip)}

/* nav */
.nav{position:absolute;left:0;top:78px;width:750px;height:30px;background:var(--green)}
.nav ul{list-style:none;display:flex;position:absolute;left:63px;top:0;height:30px}
.nav li{font-family:"Arimo",sans-serif;font-size:9px;color:#fff;height:30px;line-height:30px;text-align:center;border-right:1px solid rgba(255,255,255,.18)}
.nav li.active{background:var(--green-dark);border-top:2px solid var(--gold);line-height:26px}
.search{position:absolute;left:541px;top:9px;width:124px;height:14px;background:#fff}
.search-go{position:absolute;left:669px;top:9px;width:22px;height:14px;background:#3f6b12;color:#fff;font-family:"Arimo",sans-serif;font-size:7.5px;font-weight:700;text-align:center;line-height:14px}

/* hero */
.hero{position:absolute;left:0;top:108px;width:750px;height:277px;background:linear-gradient(180deg,#c9a43e 0%,#cfae52 55%,#c29b34 100%)}
.hero-photo{position:absolute;left:0;top:0}
.hero-brand{position:absolute;left:441px;top:45px;display:flex;align-items:center;gap:8px}
.hero-brand .brand-dot{width:34px;height:34px;background:#fff}
.hero-brand .brand-name{color:#fff;font-size:22px}
.hero h1{position:absolute;left:440px;top:107px;font-family:"Arimo",sans-serif;font-size:17px;color:#fff}
.hero p{position:absolute;left:440px;top:132px;width:225px;font-family:"Arimo",sans-serif;font-size:8.6px;line-height:12.4px;color:#fff}
.btn{position:absolute;left:440px;top:207px;width:82px;height:25px;background:var(--gold-btn);border-bottom:2px solid #b88a1c;color:#fff;font-size:8.5px;font-weight:600;letter-spacing:.4px;text-align:center;line-height:24px}

/* welcome */
.band{position:absolute;height:10px;background:var(--band)}
.welcome-title{position:absolute;left:0;width:750px;top:405px;text-align:center;font-family:"Arimo",sans-serif;font-size:16px;color:var(--green)}
.welcome-title b{font-weight:400;color:var(--green-deep)}
.welcome-text{position:absolute;left:90px;width:570px;top:437px;text-align:center;font-size:7.6px;line-height:12.6px;color:#444}
.welcome-text p+p{margin-top:12px}

/* section headings */
.sec-title{position:absolute;top:570px;font-family:"Roboto Condensed",sans-serif;font-size:16px;color:#333;background:#fff;padding-right:6px}

/* faq */
.faq-open{position:absolute;left:63px;top:611px;width:412px;height:24px;background:var(--green);color:#fff;font-size:7.5px;font-weight:600;line-height:24px;padding-left:27px}
.toggle{position:absolute;left:10px;top:9px;width:10px;height:6px;border:1.3px solid currentColor;border-radius:4px}
.toggle::after{content:"";position:absolute;left:1px;top:.5px;width:3px;height:3px;border-radius:50%;background:currentColor}
.faq-body{position:absolute;left:68px;top:646px;width:392px;font-size:6.8px;line-height:14px;color:var(--muted)}
.faq-body em{font-style:normal;color:var(--green)}
.faq-item{position:absolute;left:63px;width:412px;height:24px;background:#f2f2f2;border-left:3px solid #ddd;font-size:7.2px;color:#333;line-height:24px;padding-left:24px}
.faq-item .toggle{left:8px;color:#444}

/* hours */
.hours{position:absolute;left:491px;top:610px;width:197px;list-style:none}
.hours li{height:25.6px;border-bottom:1px solid var(--line);display:flex;align-items:center;font-size:7.6px;color:#666}
.hours li:last-child{border-bottom:none}
.hours svg{margin-right:7px}
.hours .time{margin-left:auto}
.note{position:absolute;left:491px;top:776px;width:200px;font-size:6.4px;line-height:13.5px;color:var(--muted)}
.note b{color:#444}

/* instructors */
.instructors{position:absolute;left:0;top:877px;width:750px;height:253px;background:linear-gradient(160deg,#fafafa,#f0f0f0 50%,#f8f8f8);border-top:1px solid #e6e6e6}
.instructors h2{position:absolute;left:0;width:750px;top:20px;text-align:center;font-family:"Arimo",sans-serif;font-size:15.5px;color:#333;letter-spacing:.3px}
.card{position:absolute;top:68px;width:128px}
.card .photo{height:110px;border:2px solid #fff}
.card .label{height:43px;background:var(--card);text-align:center;font-family:"Arimo",sans-serif;padding-top:6px}
.card .role{font-size:7.2px;color:var(--green-dark)}
.card .name{font-size:8.6px;color:#222;margin-top:2px;letter-spacing:.2px}
.card .more{font-size:6.4px;color:#fff;font-style:italic;font-weight:700;margin-top:2px}

/* footer */
.footer{position:absolute;left:0;top:1130px;width:750px;height:70px;background:var(--footer)}
.badge{position:absolute;top:15px;background:#8a8a8a}
.social{position:absolute;top:13px;width:20px;height:20px;border-radius:50%;background:var(--chip)}
.copy{position:absolute;left:372px;top:44px;font-family:"Arimo",sans-serif;font-size:7.4px;color:#fff}
</style>
</head>
<body>

<header>
  <div class="brand"><span class="brand-dot"></span><span class="brand-name">bright core flow</span></div>
  <div class="contact">
    <div><svg width="8" height="7" viewBox="0 0 8 7"><rect x="0" y="1" width="8" height="2" rx="1" fill="#222"/><rect x="1.5" y="3" width="5" height="4" fill="#222"/></svg>Ph: (555) 555-0142 (Toll Free)</div>
    <div><svg width="8" height="8" viewBox="0 0 8 8"><path d="M1 .5l2 0 .6 2-1 .8a5 5 0 0 0 2.1 2.1l.8-1 2 .6 0 2c-3.8.5-7-2.7-6.5-6.5z" fill="#222"/></svg>Ph: (555) 555-0142</div>
  </div>
  <div class="follow"><span>Follow Us -</span><i></i><i></i><i></i><i></i></div>
</header>

<nav class="nav">
  <ul>
    <li class="active" style="width:57px">HOME</li>
    <li style="width:100px">SCHEDULE</li>
    <li style="width:121px">INSTRUCTORS</li>
    <li style="width:70px;border-right:none">RATES</li>
  </ul>
  <div class="search"></div>
  <div class="search-go">GO</div>
</nav>

<section class="hero">
  <svg class="hero-photo" width="452" height="277" role="img" aria-label="Photo of two students doing a Pilates mat exercise with resistance bands in the studio">
    <defs><linearGradient id="heroPhoto" x1="0" y1="0" x2="0.6" y2="1"><stop offset="0" stop-color="#a9a399"/><stop offset=".45" stop-color="#8a7b6e"/><stop offset=".75" stop-color="#9a4a4a"/><stop offset="1" stop-color="#4a3a38"/></linearGradient></defs>
    <polygon points="0,0 451,0 350,277 0,277" fill="url(#heroPhoto)"/>
  </svg>
  <div class="hero-brand"><span class="brand-dot"></span><span class="brand-name">bright core flow</span></div>
  <h1>PILATES &amp; SPIRAL MOTION</h1>
  <p>simply dummy text of the printing and typesetting industry. Lorem Ipsum has been the industry's standard dummy text ever since the 1500s, when an unknown printer took a galley of type and scrambled it to make a type specimen book.</p>
  <div class="btn">READ MORE</div>
</section>

<section>
  <div class="band" style="left:63px;top:410px;width:164px"></div>
  <div class="band" style="left:522px;top:410px;width:166px"></div>
  <h2 class="welcome-title">WELCOME <b>TO BRIGHT CORE FLOW</b></h2>
  <div class="welcome-text">
    <p>Bright Core Flow Pilates and Spiral Motion® Studio, in the heart of Harbor Village, is a warm, inviting studio where students and teachers alike are supported and encouraged to discover and grow at an individual pace through the field of integrated movement.<br>We offer one-on-one sessions, group reformer classes and mat classes.</p>
    <p>Our mission is to promote long-term emotional and physical health through joyful, integrated movement training and to inspire and nurture our clients to learn more deeply about themselves and connect with fellow students and the community.</p>
  </div>
</section>

<section>
  <div class="band" style="left:292px;top:576px;width:183px"></div>
  <h2 class="sec-title" style="left:63px">GENERAL FITNESS RELATED FAQ'S</h2>
  <div class="faq-open"><span class="toggle"></span>3 days a week program</div>
  <p class="faq-body">There are many <em>variations of passages</em> of Lorem Ipsum available, but the majority have suffered alteration in some form, by injected humour, or randomised words which don't look even slightly believable. If you are going to use a passage of Lorem Ipsum, you need to be sure there isn't anything embarrassing hidden in the middle of text. All the Lorem Ipsum generators on the Internet tend to repeat predefined chunks as necessary, making this the first <em>true</em> generator on the Internet. It uses a dictionary of over 200 Latin words, combined with a handful of model.</p>
  <div class="faq-item" style="top:728px"><span class="toggle"></span>Diet program Included</div>
  <div class="faq-item" style="top:753px"><span class="toggle"></span>Professional Trainers</div>
  <div class="faq-item" style="top:778px"><span class="toggle"></span>Convienent Timing</div>
</section>

<section>
  <div class="band" style="left:610px;top:576px;width:78px"></div>
  <h2 class="sec-title" style="left:491px">WORKING HOURS</h2>
  <ul class="hours">
    <li><svg width="8" height="8" viewBox="0 0 8 8"><circle cx="4" cy="4" r="3.3" fill="none" stroke="#666" stroke-width="1.1"/><path d="M4 2v2h1.6" fill="none" stroke="#666"/></svg>Monday<span class="time">04:00 - 20:00</span></li>
    <li><svg width="8" height="8" viewBox="0 0 8 8"><circle cx="4" cy="4" r="3.3" fill="none" stroke="#666" stroke-width="1.1"/><path d="M4 2v2h1.6" fill="none" stroke="#666"/></svg>Tuesday<span class="time">04:00 - 20:00</span></li>
    <li><svg width="8" height="8" viewBox="0 0 8 8"><circle cx="4" cy="4" r="3.3" fill="none" stroke="#666" stroke-width="1.1"/><path d="M4 2v2h1.6" fill="none" stroke="#666"/></svg>wednesday<span class="time">05:00 - 20:00</span></li>
    <li><svg width="8" height="8" viewBox="0 0 8 8"><circle cx="4" cy="4" r="3.3" fill="none" stroke="#666" stroke-width="1.1"/><path d="M4 2v2h1.6" fill="none" stroke="#666"/></svg>Thursday<span class="time">05:00 - 20:00</span></li>
    <li><svg width="8" height="8" viewBox="0 0 8 8"><circle cx="4" cy="4" r="3.3" fill="none" stroke="#666" stroke-width="1.1"/><path d="M4 2v2h1.6" fill="none" stroke="#666"/></svg>Friday<span class="time">06:00 - 20:00</span></li>
    <li><svg width="8" height="8" viewBox="0 0 8 8"><circle cx="4" cy="4" r="3.3" fill="none" stroke="#666" stroke-width="1.1"/><path d="M4 2v2h1.6" fill="none" stroke="#666"/></svg>Saturday<span class="time">06:00 - 20:00</span></li>
  </ul>
  <p class="note"><b>Note:</b> At vero eos et accusamus et iusto odio dignissimos ducimus qui blanditiis praesentium will be presented.</p>
</section>

<section class="instructors">
  <h2>OUR INSTRUCTORS</h2>
  <div class="card" style="left:80px"><div class="photo" role="img" aria-label="Portrait photo of instructor Mara Ellison in the studio" style="background:linear-gradient(180deg,#cfc6b6,#b99d86 55%,#2c2a2a)"></div><div class="label"><div class="role">Pilates and Spiral Motion</div><div class="name">MARA ELLISON</div><div class="more">Read more »</div></div></div>
  <div class="card" style="left:230px"><div class="photo" role="img" aria-label="Portrait photo of instructor Tova Reyes in the studio" style="background:linear-gradient(180deg,#3a3430,#c7a08c 45%,#f2f2f2)"></div><div class="label"><div class="role">Pilates and Dance</div><div class="name">TOVA REYES</div><div class="more">Read more »</div></div></div>
  <div class="card" style="left:381px"><div class="photo" role="img" aria-label="Portrait photo of instructor Jenna Halvorsen in the studio" style="background:linear-gradient(180deg,#d9d2c6,#c79a80 55%,#3a3230)"></div><div class="label"><div class="role">Classical Method</div><div class="name">JENNA HALVORSEN</div><div class="more">Read more »</div></div></div>
  <div class="card" style="left:535px"><div class="photo" role="img" aria-label="Portrait photo of instructor Lina Castell in the studio" style="background:linear-gradient(180deg,#2e2a28,#b88e78 50%,#1f1c1c)"></div><div class="label"><div class="role">Yoga Instructor</div><div class="name">LINA CASTELL</div><div class="more">Read more »</div></div></div>
</section>

<footer class="footer">
  <div class="badge" style="left:70px;width:36px;height:40px;border-radius:3px"></div>
  <div class="badge" style="left:117px;width:40px;height:40px;border-radius:50%"></div>
  <div class="badge" style="left:168px;width:40px;height:40px;border-radius:50%"></div>
  <div class="badge" style="left:219px;width:38px;height:38px;border-radius:3px"></div>
  <div class="social" style="left:588px"></div>
  <div class="social" style="left:611px"></div>
  <div class="social" style="left:634px"></div>
  <div class="social" style="left:657px"></div>
  <p class="copy">©2015 Bright Core Flow Pilates and Spiral Motion® Studio &nbsp;| Terms of Use | Privacy Policy</p>
</footer>

</body>
</html>
```